Civic Shieldpoint Company

We have design at www.vexaloft.com and want
New site design
Carallax
Images added
Were looking for your eyes. Just placement and look and feel. No hard coding. Design only.

Industry/Entity Type

It Company

```html
<!DOCTYPE html>
<html lang="en">
<head>
<meta charset="utf-8">
<title>Vexaloft – ID Monitoring &amp; Surveillance</title>
<link href="https://fonts.googleapis.com/css2?family=Source+Sans+3:wght@400;600;700&display=swap" rel="stylesheet">
<style>
:root{
  --red:#e8090f;
  --red-soft:rgba(232,20,25,.82);
  --ink:#333;
  --muted:#6a6a6a;
  --grey-btn:#54565c;
  --grey-btn-text:#b9bbbf;
  --rule:#dcdcdc;
  --panel:#f4f4f4;
  --footer:#6f6f6f;
  --white:#fff;
}
*{box-sizing:border-box;margin:0;padding:0}
html,body{width:1200px;height:1087px;overflow:hidden;background:var(--white);font-family:"Source Sans 3",sans-serif;color:var(--muted)}
.page{position:relative;width:1200px;height:1087px}
.header{position:absolute;top:0;left:0;width:1200px;height:80px;border-bottom:1px solid #ddd;background:var(--white)}
.brand{position:absolute;left:182px;top:24px;font-size:30px;font-weight:700;color:var(--red);letter-spacing:.5px;line-height:34px}
.nav{position:absolute;left:449px;top:25px;display:flex;align-items:center;height:32px}
.nav a{font-size:11px;font-weight:600;color:#444;text-decoration:none;text-transform:uppercase;text-align:center}
.nav .active{background:var(--red);color:var(--white);width:80px;line-height:32px;border-radius:3px}
.nav .item{width:112px}
.signin{position:absolute;left:922px;top:25px;width:97px;height:32px;background:var(--grey-btn);color:var(--grey-btn-text);border-radius:3px;font-size:12px;font-weight:600;text-align:center;line-height:32px}
.hero{position:absolute;top:80px;left:0;width:1200px;height:432px;background:linear-gradient(100deg,#e9e6e2 0%,#d8d2ca 30%,#c9c0b4 55%,#b3a79a 75%,#8a7d70 100%)}
.caption{position:absolute;right:180px;background:var(--red-soft);color:var(--white);font-weight:600;font-size:21px;line-height:38px;padding:0 24px;text-transform:uppercase}
.caption.one{top:287px}
.caption.two{top:330px}
.arrows{position:absolute;left:950px;top:383px;display:flex;gap:1px}
.arrows span{width:34px;height:34px;background:var(--red-soft);display:flex;align-items:center;justify-content:center}
.welcome{position:absolute;top:536px;left:180px;width:840px;text-align:center}
.welcome h1{font-size:19px;font-weight:600;color:var(--red);text-transform:uppercase;margin-bottom:10px}
.welcome p{font-size:10px;line-height:15px;margin-bottom:15px;padding:0 8px}
.rule{position:absolute;top:669px;left:180px;width:840px;height:1px;background:var(--rule)}
.feature{position:absolute;width:270px}
.feature .icon{position:absolute;left:0;top:0;width:40px;height:40px;border-radius:50%;background:var(--red);display:flex;align-items:center;justify-content:center}
.feature h2{margin-left:51px;font-size:12.5px;font-weight:600;color:var(--red);text-transform:uppercase;line-height:16px}
.feature p{margin-left:51px;margin-top:6px;font-size:9.5px;line-height:15.5px}
.register{position:absolute;top:896px;left:180px;width:839px;height:86px;background:var(--panel);border:1px solid #e6e6e6}
.register h3{position:absolute;left:19px;top:16px;font-size:19px;font-weight:400;color:var(--red)}
.register p{position:absolute;left:19px;top:48px;font-size:12.5px;color:var(--muted)}
.register .cta{position:absolute;left:659px;top:21px;width:159px;height:42px;background:var(--grey-btn);color:var(--grey-btn-text);font-size:16px;font-weight:600;text-align:center;line-height:42px;border-radius:3px}
.footer{position:absolute;top:1012px;left:0;width:1200px;height:75px;background:var(--footer);color:var(--white)}
.footer-nav{position:absolute;left:180px;top:19px;display:flex;font-size:8px;font-weight:600;text-transform:uppercase}
.footer-nav span.sep{margin:0 19px}
.copy{position:absolute;left:181px;top:43px;font-size:8px;font-weight:600;text-transform:uppercase}
.follow{position:absolute;left:876px;top:23px;font-size:8px;font-weight:600;text-transform:uppercase}
.social{position:absolute;left:929px;top:14px;display:flex;gap:6px}
.social span{width:26px;height:26px;border-radius:50%}
.social .a{background:#3a6bb5}.social .b{background:#4fb7e8}.social .c{background:#1f7fb0}
</style>
</head>
<body>
<div class="page">
  <header class="header">
    <div class="brand">Vexaloft</div>
    <nav class="nav">
      <a class="active">Home</a>
      <a class="item">About Us</a>
      <a class="item">Services</a>
      <a class="item">Contact Us</a>
    </nav>
    <div class="signin">SIGN IN</div>
  </header>

  <section class="hero" role="img" aria-label="Photo of a hand holding a credit card while typing on a laptop, with a wallet on the desk">
    <div class="caption one">Vexaloft is a</div>
    <div class="caption two">ID Monitoring &amp; Surveillance</div>
    <div class="arrows">
      <span><svg width="8" height="12" viewBox="0 0 8 12"><path d="M7 0 L0 6 L7 12Z" fill="#fff"/></svg></span>
      <span><svg width="8" height="12" viewBox="0 0 8 12"><path d="M1 0 L8 6 L1 12Z" fill="#fff"/></svg></span>
    </div>
  </section>

  <section class="welcome">
    <h1>Welcome to Vexaloft</h1>
    <p>Assisted Recovery - This means the organization will assist you in recovering your ID. This is accomplished through coaching, providing details of the agencies you need to contact, forms, etc. You are the person applying the effort to restore your identity. This will require countless hours of your time. Better than nothing.</p>
    <p>Complete Restoration - This means the organization will act on your behalf to restore your identity for you. This is accomplished by signing paperwork giving the recovery specialist the ability to act on your behalf and work for you to recover your identity to pre-theft status. This requires minimal effort as they do the work for you. The Best Choice!</p>
  </section>
  <div class="rule"></div>

  <article class="feature" style="left:180px;top:705px">
    <div class="icon"><svg width="20" height="18" viewBox="0 0 20 18"><rect x="1" y="1" width="18" height="11" fill="none" stroke="#fff" stroke-width="2"/><rect x="8" y="12" width="4" height="3" fill="#fff"/><rect x="5" y="15" width="10" height="2" fill="#fff"/></svg></div>
    <h2>ID Monitoring &amp; Surveillance</h2>
    <p>Scanning engines, human intelligence gathering and mathematical algorithms find and analyze your data online.</p>
  </article>
  <article class="feature" style="left:474px;top:705px">
    <div class="icon"><svg width="14" height="24" viewBox="0 0 14 24"><path d="M7 1v22M12 6c-1-2-3-2.5-5-2.5S2 4.5 2 7s3 3.5 5 4 5 1.5 5 4-2 3.5-5 3.5-4.5-1-5.5-3" fill="none" stroke="#fff" stroke-width="1.8"/></svg></div>
    <h2>$25,000 Loss Insurance</h2>
    <p>Identity Fraud Loss and Expense Reimbursement Master Policy from Harrowmere Insurance is designed to...</p>
  </article>
  <article class="feature" style="left:758px;top:705px">
    <div class="icon"><svg width="20" height="16" viewBox="0 0 20 16"><rect x="1" y="3" width="18" height="12" rx="1" fill="#fff"/><path d="M3 3 L14 0 L15 3" fill="#fff"/><rect x="13" y="7" width="6" height="4" fill="#e8090f"/></svg></div>
    <h2>Lost Wallet Service</h2>
    <p>Store information about the contents of your purse and wallet securely. If ever lost or stolen, you are protected</p>
  </article>
  <article class="feature" style="left:180px;top:803px">
    <div class="icon"><svg width="20" height="20" viewBox="0 0 20 20"><path d="M4 8 L10 3 L16 6 L15 15 L8 17 L4 13Z" fill="#fff"/><path d="M8 8 L12 12" stroke="#e8090f" stroke-width="1.5"/></svg></div>
    <h2>Identity Theft Recovery</h2>
    <p>If your identity is stolen, we recover your ID for you or assist you in your recovery - your choice.</p>
  </article>
  <article class="feature" style="left:474px;top:803px">
    <div class="icon"><svg width="22" height="18" viewBox="0 0 22 18"><rect x="1" y="1" width="16" height="11" rx="1" fill="none" stroke="#fff" stroke-width="1.8"/><rect x="5" y="6" width="16" height="11" rx="1" fill="#fff"/><rect x="5" y="9" width="16" height="2" fill="#e8090f"/></svg></div>
    <h2>ID vs Credit Monitoring</h2>
    <p>Identity scoring and monitoring is more effective than credit report monitoring. Study by Tellwick Group.</p>
  </article>
  <article class="feature" style="left:758px;top:803px">
    <div class="icon"><svg width="18" height="20" viewBox="0 0 18 20"><circle cx="9" cy="5" r="4" fill="#fff"/><path d="M1 19 C1 12 17 12 17 19Z" fill="#fff"/><path d="M9 11 L8 17 L9 18 L10 17Z" fill="#e8090f"/></svg></div>
    <h2>Faces of ID Theft</h2>
    <p>Criminals use sophisticated methods to obtain and misuse our personal information.</p>
  </article>

  <section class="register">
    <h3>Register Now</h3>
    <p>Scanning engines, human intelligence gathering and mathematical algorithms find and analyze your data online.</p>
    <div class="cta">GET STARTED</div>
  </section>

  <footer class="footer">
    <div class="footer-nav">
      <span>Home</span><span class="sep">|</span><span>About Us</span><span class="sep">|</span><span>Services</span><span class="sep">|</span><span>Contact Us</span><span class="sep">|</span><span>Sign In</span>
    </div>
    <div class="copy">Copyrights © 2013. Vexaloft. All rights reserved.</div>
    <div class="follow">Follow us :</div>
    <div class="social"><span class="a"></span><span class="b"></span><span class="c"></span></div>
  </footer>
</div>
</body>
</html>
```